Need to make a KTR water label for my water bottle and packaging. Attached is our Trademarked LOGO for KTR we have a natural spring water that flows through our land that is naturally filtered through pure limestone. want to make a badass label that has our logo in it with our colors

Target Market(s)

Commercial Bottle water

Colors
3176b5

```html
<!DOCTYPE html>
<html lang="en">
<head>
<meta charset="utf-8">
<title>KTR Pure Water Label</title>
<link rel="stylesheet" href="https://fonts.googleapis.com/css2?family=Oswald:wght@200;500;700&display=swap">
<style>
  :root {
    --brand-blue: #3176b5;
    --canvas-bg: #ffffff;
    --hill-light: #5fbf62;
    --hill-mid: #2f8a3e;
    --hill-deep: #1d5a2a;
    --forest-dark: #0f2a10;
    --label-green: #063a0b;
    --water-clear: #e6f1f9;
    --text-white: #ffffff;
  }
  * { margin: 0; padding: 0; box-sizing: border-box; }
  html, body { width: 1131px; height: 1200px; overflow: hidden; background: var(--canvas-bg); }
  .canvas { position: relative; width: 1131px; height: 1200px; }
  .label {
    position: absolute; left: 215px; top: 170px; width: 700px; height: 860px;
    font-family: "Oswald", sans-serif;
  }
  .brand-mark {
    position: absolute; left: 0; right: 0; top: 0; height: 250px;
    display: flex; align-items: center; justify-content: center; gap: 24px;
  }
  .brand-mark__dot {
    width: 44px; height: 44px; border-radius: 50%; background: var(--brand-blue);
  }
  .brand-mark__name {
    font-family: "Oswald", sans-serif; font-weight: 700; font-size: 150px;
    line-height: 1; color: var(--brand-blue); letter-spacing: 4px;
  }
  .landscape {
    position: absolute; left: 0; top: 230px; width: 700px; height: 270px;
    background: linear-gradient(180deg, var(--hill-light) 0%, var(--hill-mid) 45%, var(--hill-deep) 75%, var(--forest-dark) 100%);
  }
  .pure-band {
    position: absolute; left: 0; top: 500px; width: 700px; height: 80px;
    background: var(--forest-dark);
  }
  .word-pure {
    position: absolute; left: 0; right: 0; top: 420px; text-align: center;
    font-weight: 200; font-size: 150px; line-height: 1; color: var(--text-white);
    letter-spacing: 2px;
  }
  .water-band {
    position: absolute; left: 0; top: 580px; width: 700px; height: 180px;
    background: var(--water-clear);
  }
  .word-water {
    position: absolute; left: 0; right: 0; top: 575px; text-align: center;
    font-weight: 700; font-size: 172px; line-height: 1; color: var(--label-green);
  }
  .tagline {
    position: absolute; left: 0; top: 760px; width: 700px; height: 86px;
    background: var(--label-green); color: var(--text-white);
    display: flex; align-items: center; justify-content: center;
    font-weight: 500; font-size: 40px; letter-spacing: 0.5px;
  }
</style>
</head>
<body>
<main class="canvas">
  <section class="label">
    <div class="landscape" role="img" aria-label="Illustration of layered green forested mountains"></div>
    <div class="pure-band"></div>
    <div class="brand-mark">
      <span class="brand-mark__dot"></span>
      <span class="brand-mark__name">KTR</span>
    </div>
    <p class="word-pure">PURE</p>
    <div class="water-band"></div>
    <p class="word-water">WATER</p>
    <p class="tagline">PREMIUM SPRING MINERAL WATER</p>
  </section>
</main>
</body>
</html>
```